Kindred Stretch - Logo and Business card design

I require a business card design for my Yoga teaching business. I have a design for a logo I would like to use on the card. I would like the logo designed and provided to me separately to the business card in a jpg or tiff high resolution file so I can use this for a web site, letter head, banner in the future.
I am a travelling yoga teacher in Sydney and teach at several gyms, corporates, private clients, schools, yoga studios etc
With the design I have sent thru as a guide,I would like my own text and colours inside this logo. I have a very good idea of how I would like this to look the logo and business name on the front and contact details on the back.

Target Market(s)

Private clients, corporates, schools, gyms, studios, healthcare industry

Industry/Entity Type

Teacher

Requirements
Must have
• What is compulsory is the information sent in the uploaded file
This card must have a feel for the regular yogi to a beginner so that anyone can practice yoga and feel fantastic.
Nice to have
• refer to attached file
Should not have
• I really do not want this to be a boring Yoga card that does not relate to the average person.

```html
<!DOCTYPE html>
<html lang="en">
<head>
<meta charset="utf-8">
<title>Kindred Stretch – Business Card</title>
<link href="https://fonts.googleapis.com/css2?family=Raleway:wght@400;700&family=Roboto+Condensed:wght@700&display=swap" rel="stylesheet">
<style>
  :root {
    --page: #ffffff;
    --pink-deep: #cf66a4;
    --pink-mid: #e3a6ca;
    --pink-light: #f8edf4;
    --brand: #b4508d;
    --ink: #2f2f2f;
    --ink-soft: #444444;
    --divider: #ffffff;
  }
  * { margin: 0; padding: 0; box-sizing: border-box; }
  html, body { width: 1200px; height: 1145px; overflow: hidden; background: var(--page); }
  .canvas { position: relative; width: 1200px; height: 1145px; }

  .card {
    position: absolute;
    left: 150px;
    width: 778px;
    height: 435px;
    border-radius: 26px;
    box-shadow: 0 4px 14px rgba(0,0,0,0.28);
    overflow: hidden;
  }
  .card--front {
    top: 105px;
    background: linear-gradient(90deg, var(--pink-deep) 0%, var(--pink-light) 30%, var(--pink-mid) 70%, var(--pink-deep) 100%);
  }
  .card--back {
    top: 606px;
    background: linear-gradient(90deg, var(--pink-deep) 0%, var(--pink-mid) 22%, var(--pink-light) 50%, var(--pink-mid) 78%, var(--pink-deep) 100%);
  }

  .logo-art {
    position: absolute;
    left: 237px;
    top: 30px;
    width: 285px;
    height: 330px;
  }
  .brand-name {
    position: absolute;
    left: 0;
    width: 100%;
    top: 372px;
    text-align: center;
    font-family: "Roboto Condensed", sans-serif;
    font-weight: 700;
    font-size: 26px;
    color: var(--brand);
    letter-spacing: 0.5px;
  }

  .identity {
    position: absolute;
    right: 418px;
    top: 150px;
    text-align: right;
    font-family: "Raleway", sans-serif;
    color: var(--ink-soft);
  }
  .identity__name { font-weight: 700; font-size: 30px; color: var(--ink); margin-bottom: 16px; }
  .identity__role { font-size: 21px; line-height: 29px; }
  .identity__abn { font-size: 15px; margin-top: 14px; }

  .divider {
    position: absolute;
    left: 364px;
    top: 110px;
    width: 4px;
    height: 220px;
    background: linear-gradient(180deg, transparent, var(--divider) 20%, var(--divider) 80%, transparent);
  }

  .contact {
    position: absolute;
    left: 380px;
    top: 150px;
    font-family: "Raleway", sans-serif;
    color: var(--ink);
  }
  .contact__title { font-size: 21px; color: var(--ink-soft); margin-bottom: 30px; }
  .contact__line { display: flex; align-items: center; gap: 8px; font-weight: 700; font-size: 22px; margin-bottom: 16px; }
  .contact__icon { width: 18px; height: 18px; flex: none; }
</style>
</head>
<body>
<main class="canvas">

  <section class="card card--front" aria-label="Card front">
    <svg class="logo-art" viewBox="0 0 285 330" role="img" aria-label="Seated meditating figure filled with colourful yoga words">
      <defs>
        <linearGradient id="art-fill" x1="0" y1="0" x2="1" y2="1">
          <stop offset="0" stop-color="#e05a9a"/>
          <stop offset="0.35" stop-color="#f2a23a"/>
          <stop offset="0.65" stop-color="#4fb06a"/>
          <stop offset="1" stop-color="#3a8fd0"/>
        </linearGradient>
      </defs>
      <rect x="0" y="0" width="285" height="330" rx="40" fill="url(#art-fill)" opacity="0.55"/>
    </svg>
    <div class="brand-name">KINDRED STRETCH</div>
  </section>

  <section class="card card--back" aria-label="Card back">
    <div class="identity">
      <div class="identity__name">MAYA HOLT</div>
      <div class="identity__role">Advanced Flow Balance<br>Instructor</div>
      <div class="identity__abn">ABN: 12 345 678 901</div>
    </div>

    <div class="divider"></div>

    <div class="contact">
      <div class="contact__title">Certified Vinyasa Yoga Teacher</div>
      <div class="contact__line">
        <svg class="contact__icon" viewBox="0 0 24 24" aria-hidden="true"><path fill="#2f2f2f" d="M6.6 10.8a15.1 15.1 0 0 0 6.6 6.6l2.2-2.2a1 1 0 0 1 1-.25 11.4 11.4 0 0 0 3.6.57 1 1 0 0 1 1 1V20a1 1 0 0 1-1 1A17 17 0 0 1 3 4a1 1 0 0 1 1-1h3.5a1 1 0 0 1 1 1c0 1.25.2 2.45.57 3.57a1 1 0 0 1-.25 1z"/></svg>
        <span>0400 123 456</span>
      </div>
      <div class="contact__line">
        <svg class="contact__icon" viewBox="0 0 24 24" aria-hidden="true"><rect x="2.5" y="5" width="19" height="14" rx="1.5" fill="none" stroke="#2f2f2f" stroke-width="1.8"/><path d="M3 6l9 7 9-7" fill="none" stroke="#2f2f2f" stroke-width="1.8"/></svg>
        <span>hello@kindredstretch.com</span>
      </div>
    </div>
  </section>

</main>
</body>
</html>
```